Postcard Design

I have an accounting firm and I would like to increase my customer base by a postcard mailout/letter dropI want a design that is eye catching and uses my logo. I specialise in small to medium business and offer services for commercial accounting and business advisory. I also want to offer a discount for new clients.Previously I had my website updated and would like to stay with the theme

Industry/Entity Type

Business Consultant

Font styles to use
Serif

Colors
b667aa
d3a5cc

Requirements
Must have
• the post card needs to be arty to attract attention. also business like

```html
<!DOCTYPE html>
<html lang="en">
<head>
<meta charset="utf-8">
<title>Marlow Accounting Services – Postcard</title>
<link rel="stylesheet" href="https://fonts.googleapis.com/css2?family=Cabin:ital,wght@0,400;0,500;0,600;1,600&family=Delius+Swash+Caps&display=swap">
<style>
  :root {
    --purple: #b667aa;
    --purple-deep: #9a3f9a;
    --lilac: #d3a5cc;
    --ink-purple: #6a1f8a;
    --grey: #5c5c5c;
    --grey-dark: #3f3f3f;
    --white: #ffffff;
    --page: #ffffff;
  }
  * { margin: 0; padding: 0; box-sizing: border-box; }
  html, body { width: 776px; height: 1200px; overflow: hidden; background: var(--page); }
  body { position: relative; font-family: "Cabin", sans-serif; }

  .card {
    position: absolute;
    left: 26px;
    width: 724px;
    background: var(--white);
    overflow: hidden;
    border: 1px solid #e2e2e2;
  }
  .card--front { top: 26px; height: 569px; }
  .card--back { top: 614px; height: 561px; }

  /* Front */
  .front-photo {
    position: absolute; left: 0; top: 0; width: 724px; height: 400px;
    background: linear-gradient(160deg, #dfe9f3 0%, #f4f7fb 40%, #c9d6e4 75%, #8e8a86 100%);
  }
  .front-wave { position: absolute; left: 0; top: 290px; width: 724px; height: 140px; }
  .brand-dot {
    position: absolute; border-radius: 50%;
    background: var(--lilac);
  }
  .card--front .brand-dot { left: 36px; top: 392px; width: 108px; height: 108px; }
  .front-name {
    position: absolute; left: 175px; top: 406px;
    font-size: 36px; font-weight: 400; color: var(--grey);
    font-variant: small-caps; letter-spacing: 0.5px; line-height: 1;
  }
  .front-tagline {
    position: absolute; left: 177px; top: 452px;
    font-family: "Delius Swash Caps", cursive;
    font-size: 21px; color: var(--purple-deep);
  }
  .front-contact {
    position: absolute; left: 178px; top: 492px;
    display: flex; align-items: center; gap: 8px;
    font-size: 27px; color: var(--grey-dark);
  }
  .front-web {
    position: absolute; left: 395px; top: 502px;
    display: flex; align-items: center; gap: 9px;
    font-size: 11px; letter-spacing: 0.6px; color: var(--grey-dark); text-transform: uppercase;
  }

  /* Back */
  .back-photo {
    position: absolute; left: 0; top: 80px; width: 372px; height: 422px;
    background: linear-gradient(135deg, #f7f7fa 0%, #e7ebf2 45%, #d7dbe2 70%, #eef1f5 100%);
  }
  .back-header { position: absolute; left: 0; top: 0; width: 724px; height: 160px; }
  .card--back .brand-dot { left: 28px; top: 28px; width: 82px; height: 82px; background: rgba(255,255,255,0.45); }
  .back-name {
    position: absolute; left: 121px; top: 30px;
    font-size: 27px; font-weight: 400; color: var(--white); font-variant: small-caps; letter-spacing: 0.5px;
  }
  .back-phone {
    position: absolute; left: 125px; top: 68px;
    display: flex; align-items: center; gap: 6px;
    font-size: 23px; color: var(--white);
  }
  .return-address {
    position: absolute; left: 394px; top: 94px;
    font-size: 12.5px; line-height: 19px; color: var(--grey-dark); font-style: normal;
  }
  .stamp-box {
    position: absolute; left: 601px; top: 38px; width: 96px; height: 114px;
    border: 2px dashed var(--ink-purple);
  }
  .address-line {
    position: absolute; left: 389px; width: 318px;
    border-top: 2px dashed var(--ink-purple);
  }

  .offer {
    position: absolute; left: 23px; top: 158px; width: 350px;
    color: var(--ink-purple);
  }
  .offer-intro { font-style: italic; font-weight: 600; font-size: 15px; line-height: 20px; margin-bottom: 3px; }
  .offer-heading { font-size: 15px; font-weight: 500; text-decoration: underline; line-height: 20px; }
  .offer-list { list-style: none; font-size: 15px; font-weight: 500; line-height: 20px; }
  .offer-list li { position: relative; padding-left: 33px; }
  .offer-list li::before {
    content: ""; position: absolute; left: 3px; top: 8px;
    width: 5px; height: 5px; border-radius: 50%; background: var(--ink-purple);
  }

  .feature-art {
    position: absolute; left: 20px; top: 440px; width: 340px; height: 106px;
    background: linear-gradient(100deg, var(--lilac) 0%, #c98bbf 50%, var(--purple) 100%);
    opacity: 0.85;
  }
</style>
</head>
<body>

<section class="card card--front">
  <div class="front-photo" role="img" aria-label="Photograph of a business team meeting around a table with a bar chart on a wall screen"></div>
  <svg class="front-wave" viewBox="0 0 724 140" preserveAspectRatio="none" aria-hidden="true">
    <path d="M0 25 C160 20 330 100 520 100 C620 100 690 70 724 50 L724 140 L0 140 Z" fill="#d3a5cc"/>
    <path d="M0 32 C160 30 330 110 520 108 C620 106 690 80 724 62 L724 106 C640 95 560 90 470 98 C320 108 170 118 0 114 Z" fill="#b667aa"/>
    <path d="M0 114 C170 118 320 108 470 98 C560 90 640 95 724 106 L724 140 L0 140 Z" fill="#ffffff"/>
  </svg>
  <div class="brand-dot" aria-hidden="true"></div>
  <h1 class="front-name">Marlow Accounting Services</h1>
  <p class="front-tagline">The Accountants with Professional Integrity</p>
  <p class="front-contact">
    <svg width="26" height="26" viewBox="0 0 26 26" aria-hidden="true"><circle cx="13" cy="13" r="11.5" fill="none" stroke="#3f3f3f" stroke-width="2"/><path d="M9 7 C6 10 9 17 15 20 L18 17 L15.5 15 L14 16 C12 15 11 14 10 12 L11.5 10.5 L10 7 Z" fill="#3f3f3f"/></svg>
    02 4000 1234
  </p>
  <p class="front-web">
    <svg width="12" height="12" viewBox="0 0 12 12" aria-hidden="true"><circle cx="6" cy="6" r="5.3" fill="none" stroke="#3f3f3f" stroke-width="1.2"/><rect x="5.4" y="5" width="1.2" height="4" fill="#3f3f3f"/><circle cx="6" cy="3.4" r="0.8" fill="#3f3f3f"/></svg>
    www.marlowaccountingservices.com
  </p>
</section>

<section class="card card--back">
  <div class="back-photo" role="img" aria-label="Faded photograph of hands working with a calculator and financial papers"></div>
  <svg class="back-header" viewBox="0 0 724 160" aria-hidden="true">
    <path d="M0 0 H724 V125 C700 100 660 76 600 72 C520 68 440 70 380 80 C300 96 200 148 100 154 L0 154 Z" fill="#b667aa"/>
  </svg>
  <div class="brand-dot" aria-hidden="true"></div>
  <h2 class="back-name">Marlow Accounting Services</h2>
  <p class="back-phone">
    <svg width="22" height="22" viewBox="0 0 26 26" aria-hidden="true"><circle cx="13" cy="13" r="11.5" fill="none" stroke="#ffffff" stroke-width="2"/><path d="M9 7 C6 10 9 17 15 20 L18 17 L15.5 15 L14 16 C12 15 11 14 10 12 L11.5 10.5 L10 7 Z" fill="#ffffff"/></svg>
    02 4000 1234
  </p>
  <address class="return-address">
    Level 2, 40 Harbour Lane,<br>Newcastle NSW<br>Australia 2300
  </address>
  <div class="stamp-box" aria-label="Stamp area"></div>
  <div class="address-line" style="top:296px"></div>
  <div class="address-line" style="top:365px"></div>
  <div class="address-line" style="top:434px"></div>

  <div class="offer">
    <p class="offer-intro">As Business Advisory and Commercial Accountant we welcome the opportunity to earn your trust and deliver the best service in the industry.</p>
    <h3 class="offer-heading">WE SERVE</h3>
    <ul class="offer-list">
      <li>Mid North Coast of New South Wales</li>
      <li>Sydney CBD</li>
      <li>The Newcastle Hunter Region</li>
    </ul>
    <h3 class="offer-heading">OUR BENEFITS</h3>
    <ul class="offer-list">
      <li>We are Committed to Innovative Accounting Strategies</li>
      <li>We are Professionally Qualified Accountants</li>
      <li>We Proactively Deliver Services</li>
      <li>We Support Our Clients in Achieving Business Goals</li>
    </ul>
  </div>

  <div class="feature-art" role="img" aria-label="Decorative graphic of three tilted notes naming the firm's advice, experts and strategies"></div>
</section>

</body>
</html>
```